Packaging Design Project

My company produces chocolate bars; currently have 4 bars that are packaged in slim window boxes.

I need some product images, but the photos we've taken look awful. I think someone with solid Photoshop skills could take our electronic files and create some product images based on the digital files.

I need 4 product images. Also, if you are able to product any additional general images like this:
http://snapvelle.com/brivantcocoafan/cocoa-makes-our-recess/

```html
<!DOCTYPE html>
<html lang="en">
<head>
<meta charset="utf-8">
<title>Rosaline Cacao – Chili Pepper Bar</title>
<link rel="stylesheet" href="https://fonts.googleapis.com/css2?family=Questrial&family=PT+Sans&family=Handlee&family=Give+You+Glory&display=swap">
<style>
  :root {
    --page-bg: #ffffff;
    --box-dark: #161616;
    --box-mid: #262626;
    --band-red: #a5161a;
    --band-red-light: #b52a2c;
    --ink-light: #f2f2f2;
    --ink-soft: #d9d9d9;
    --choc-dark: #2a1512;
    --choc-mid: #4a2620;
  }
  html, body {
    margin: 0;
    padding: 0;
    width: 1200px;
    height: 1000px;
    overflow: hidden;
    background: var(--page-bg);
  }
  .canvas {
    position: relative;
    width: 1200px;
    height: 1000px;
  }
  .package {
    position: absolute;
    left: 397px;
    top: 94px;
    width: 403px;
    height: 820px;
    background: linear-gradient(180deg, var(--box-mid) 0%, var(--box-dark) 45%, var(--box-dark) 100%);
  }
  .brand {
    position: absolute;
    top: 75px;
    left: 0;
    width: 100%;
    text-align: center;
    font-family: "Questrial", sans-serif;
    color: var(--ink-light);
    font-size: 27px;
    letter-spacing: 3px;
    line-height: 1.35;
  }
  .flavour-band {
    position: absolute;
    top: 203px;
    left: 0;
    width: 100%;
    height: 50px;
    background: linear-gradient(90deg, var(--band-red) 0%, var(--band-red-light) 100%);
    display: flex;
    align-items: center;
    justify-content: center;
  }
  .flavour-name {
    font-family: "Handlee", cursive;
    color: var(--ink-light);
    font-size: 29px;
    letter-spacing: 1px;
  }
  .tagline {
    position: absolute;
    top: 276px;
    left: 0;
    width: 100%;
    text-align: center;
    font-family: "PT Sans", sans-serif;
    color: var(--ink-soft);
    font-size: 19px;
    line-height: 24px;
  }
  .product-window {
    position: absolute;
    left: 80px;
    top: 365px;
    width: 252px;
    height: 196px;
    background: linear-gradient(160deg, var(--choc-mid) 0%, var(--choc-dark) 70%);
    box-shadow: inset 0 0 0 1px #3a3a3a;
  }
  .description {
    position: absolute;
    top: 600px;
    left: 0;
    width: 100%;
    text-align: center;
    font-family: "Give You Glory", cursive;
    color: var(--ink-soft);
    font-size: 21px;
    line-height: 43px;
    letter-spacing: 1px;
  }
  .net-weight {
    position: absolute;
    top: 784px;
    left: 0;
    width: 100%;
    text-align: center;
    font-family: "PT Sans", sans-serif;
    color: var(--ink-light);
    font-size: 11px;
  }
</style>
</head>
<body>
  <main class="canvas">
    <section class="package">
      <div class="brand">ROSALINE<br>CACAO</div>
      <div class="flavour-band"><span class="flavour-name">Chili Pepper</span></div>
      <p class="tagline" style="margin:0">Spicy chili pepper with 58%<br>dark chocolate</p>
      <div class="product-window" role="img" aria-label="Window showing the dark chocolate bar segments inside"></div>
      <p class="description" style="margin:0">58% Belgium dark<br>chocolate with<br>organic chili peppers</p>
      <p class="net-weight" style="margin:0">NET WT 4 OZ (113g)</p>
    </section>
  </main>
</body>
</html>
```